Energy Company 8-page Brochure

We are in need of a redesign of our 8-page brochure. Attached is the initial design that does not represent us very well. We are looking for CLEAN/CORPORATE look with a little bit of flair (graphs/charts if applicable).

I prefer white background and our company colors (blue/green) to be the accent colors. Feel free to add additional accent colors to highlight certain areas.

We are in the energy field (not just solar), so please consider the types of images that you will use. Are headquarters is located in Chicago, IL so a great looking picture of the skyline or something similar would work for the front and back cover.

We have additional marketing collateral that we will want to be uniformed once we have the right design.

Good luck, and we look forward to receiving some great designs!

Best Regards,
Rob

Target Market(s)

Small to large businesses (B2B).

Industry/Entity Type

It Company

Colors
ffffff
9bcb3c
0255a3

Requirements
Must have
• Clean design, company colors, specified content and editable files.
Nice to have
• Graphs, charts, highlighted areas where necessary.
Should not have
• Clutter! Please utilized page space appropriately. There is a lot of content, so you need to consider graphics and image placement.

```html
<!DOCTYPE html>
<html lang="en">
<head>
<meta charset="utf-8">
<title>Everything Energy – Brochure Cover Spread</title>
<link rel="stylesheet" href="https://fonts.googleapis.com/css2?family=Source+Sans+3:wght@300;400;600;700&display=swap">
<style>
  :root {
    --backdrop: #6b7078;
    --paper: #f6f6f6;
    --swirl-light: #ffffff;
    --swirl-dark: #e4e4e4;
    --brand-blue: #0255a3;
    --brand-green: #7fae2a;
    --bulb-green: #9bcb3c;
    --text-blue: #2a5d8f;
  }
  * { margin: 0; padding: 0; box-sizing: border-box; }
  html, body { width: 1200px; height: 862px; overflow: hidden; }
  body {
    background: var(--backdrop);
    font-family: "Source Sans 3", "Myriad Pro", Arial, sans-serif;
    position: relative;
  }
  .spread {
    position: absolute; left: 58px; top: 63px; width: 1100px; height: 713px;
    background: var(--paper);
  }
  .page { position: absolute; top: 0; width: 550px; height: 713px; overflow: hidden; }
  .page--back { left: 0; }
  .page--front { left: 550px; }
  .swirl-pattern {
    position: absolute; inset: 0;
    background:
      radial-gradient(ellipse 60% 40% at 30% 30%, var(--swirl-light), transparent 70%),
      radial-gradient(ellipse 50% 35% at 70% 80%, var(--swirl-dark), transparent 70%),
      linear-gradient(160deg, var(--swirl-light) 0%, var(--paper) 45%, var(--swirl-dark) 100%);
  }

  .address { position: absolute; top: 63px; font-size: 12.5px; line-height: 14px; color: var(--text-blue); font-weight: 400; }
  .address h2 { font-size: 13.5px; font-weight: 700; color: var(--brand-blue); margin-bottom: 12px; letter-spacing: 0.1px; }
  .address p { margin-bottom: 13px; }
  .address--hq { left: 62px; }
  .address--holding { left: 276px; }

  .brand { position: absolute; display: flex; align-items: center; gap: 7px; font-weight: 600; color: var(--brand-blue); white-space: nowrap; }
  .brand__dot { border-radius: 50%; border: 3px solid var(--brand-blue); background: transparent; flex: none; }
  .brand--power { color: var(--brand-blue); }
  .brand--verda { color: var(--brand-green); }
  .brand--verda .brand__dot { border-radius: 0; border-color: var(--brand-green); }

  .brand--back-power { left: 62px; top: 596px; font-size: 15px; }
  .brand--back-power .brand__dot { width: 30px; height: 30px; }
  .brand--back-verda { left: 374px; top: 600px; font-size: 14px; }
  .brand--back-verda .brand__dot { width: 24px; height: 24px; }
  .brand--front-power { left: 44px; top: 57px; font-size: 18px; }
  .brand--front-power .brand__dot { width: 40px; height: 40px; }
  .brand--front-verda { left: 355px; top: 60px; font-size: 17px; }
  .brand--front-verda .brand__dot { width: 32px; height: 32px; }

  .bulb-illustration {
    position: absolute; left: 150px; top: 252px; width: 252px; height: 250px;
    border-radius: 48% 48% 40% 40%;
    background: radial-gradient(ellipse 45% 50% at 50% 40%, var(--bulb-green) 0%, var(--bulb-green) 55%, rgba(2,85,163,0.25) 75%, transparent 78%);
  }

  .benefit { position: absolute; text-align: center; font-size: 14.5px; line-height: 16px; color: var(--text-blue); font-weight: 400; }
  .benefit strong { font-weight: 700; color: var(--brand-blue); }
  .benefit__icon { display: block; width: 40px; height: 40px; margin: 0 auto 8px; }
  .benefit--pricing { left: 216px; top: 156px; width: 200px; }
  .benefit--cost { left: 42px; top: 309px; width: 120px; }
  .benefit--risk { left: 380px; top: 309px; width: 140px; }
  .benefit--risk .benefit__icon { margin-bottom: 10px; }
  .benefit--usage { left: 106px; top: 479px; width: 140px; }
  .benefit--values { left: 306px; top: 479px; width: 140px; }

  .headline {
    position: absolute; left: 44px; top: 590px;
    font-size: 51px; font-weight: 400; letter-spacing: 0.3px; line-height: 1;
    color: var(--brand-blue); white-space: nowrap;
  }
  .headline__accent { color: var(--brand-green); font-weight: 600; }
</style>
</head>
<body>
  <main class="spread">
    <section class="page page--back">
      <div class="swirl-pattern" role="img" aria-label="Faint white and light grey flowing swirl background"></div>

      <address class="address address--hq">
        <h2>ILLINOIS HEADQUARTERS</h2>
        <p>2240 West Lake Street<br>Suite 310<br>Chicago, IL 60612</p>
        <p>800.555.0142<br>www.brightlinepower.com<br>www.verdaefficiency.com</p>
      </address>

      <address class="address address--holding">
        <h2>CRESTMARK HOLDING CORPORATION</h2>
        <p>A Publicly Traded Energy Services<br>Company (CRMK)</p>
        <p>4710 Orchard Avenue<br>Suite B<br>Alder Grove, CA 92790<br>(949) 555-0187</p>
      </address>

      <div class="brand brand--power brand--back-power"><span class="brand__dot"></span>Brightline Power</div>
      <div class="brand brand--verda brand--back-verda"><span class="brand__dot"></span>Verda Efficiency</div>
    </section>

    <section class="page page--front">
      <div class="swirl-pattern" role="img" aria-label="Faint white and light grey flowing swirl background"></div>

      <div class="brand brand--power brand--front-power"><span class="brand__dot"></span>Brightline Power</div>
      <div class="brand brand--verda brand--front-verda"><span class="brand__dot"></span>Verda Efficiency</div>

      <div class="bulb-illustration" role="img" aria-label="Green light bulb with a blue base, circled by blue orbit rings and a white recycle arrow"></div>

      <div class="benefit benefit--pricing">
        <svg class="benefit__icon" viewBox="0 0 40 40"><circle cx="20" cy="20" r="20" fill="#0255a3"/><circle cx="20" cy="20" r="10" fill="none" stroke="#fff" stroke-width="2.5"/><text x="20" y="25" text-anchor="middle" font-size="14" font-weight="700" fill="#fff" font-family="Source Sans 3, sans-serif">$</text></svg>
        We <strong>manage<br>pricing</strong> volatility.
      </div>

      <div class="benefit benefit--cost">
        <svg class="benefit__icon" viewBox="0 0 40 40"><circle cx="20" cy="20" r="20" fill="#0255a3"/><ellipse cx="20" cy="21" rx="10" ry="7" fill="#fff"/><rect x="14" y="26" width="3" height="4" fill="#fff"/><rect x="23" y="26" width="3" height="4" fill="#fff"/><rect x="18" y="12" width="5" height="2" fill="#fff"/></svg>
        We <strong>secure</strong><br>the lowest cost.
      </div>

      <div class="benefit benefit--risk">
        <svg class="benefit__icon" viewBox="0 0 40 40"><circle cx="20" cy="20" r="20" fill="#0255a3"/><polyline points="10,15 18,23 29,12" fill="none" stroke="#fff" stroke-width="2.5"/><polyline points="22,27 30,27 30,19" fill="none" stroke="#fff" stroke-width="2.5" transform="rotate(-90 26 23)"/></svg>
        We <strong>mitigate</strong> risk.
      </div>

      <div class="benefit benefit--usage">
        <svg class="benefit__icon" viewBox="0 0 40 40"><circle cx="20" cy="20" r="20" fill="#0255a3"/><circle cx="20" cy="17" r="7" fill="none" stroke="#fff" stroke-width="2.2"/><rect x="17" y="25" width="6" height="5" fill="#fff"/></svg>
        We <strong>lower</strong><br>energy usage.
      </div>

      <div class="benefit benefit--values">
        <svg class="benefit__icon" viewBox="0 0 40 40"><circle cx="20" cy="20" r="20" fill="#0255a3"/><circle cx="20" cy="15" r="4" fill="#fff"/><polygon points="11,30 14,21 26,21 29,30" fill="none" stroke="#fff" stroke-width="2"/><line x1="20" y1="21" x2="20" y2="30" stroke="#fff" stroke-width="1.5"/><line x1="12.5" y1="25.5" x2="27.5" y2="25.5" stroke="#fff" stroke-width="1.5"/></svg>
        We <strong>reflect</strong> your<br>energy values.
      </div>

      <h1 class="headline">EVERYTHING <span class="headline__accent">ENERGY</span></h1>
    </section>
  </main>
</body>
</html>
```